Marlow Creek sign

24"x36" sign for new home construction job site. Located in affluent in-town neighborhood in Midwest. Traditional american style homes. 2nd generation construction company. Sign needs to convey strength and elegance but not overly elaborate. Competition most has signs consisting of text.

Sign text reads:
Marlow Creek Builders
Custom Luxury for Over 20 years
248-555-0137

Target Market(s)

Upper middle income home buyers

Industry/Entity Type

Construction

Font styles to use
Serif
Decorative

Requirements
Must have
• Logo image no more than 2 colors
Nice to have
• Should be visible and legible from distance of 30'
Should not have
• Not just image of house as logo

```html
<!DOCTYPE html>
<html lang="en">
<head>
<meta charset="utf-8">
<title>Marlow Creek Builders – Job Site Sign</title>
<link rel="stylesheet" href="https://fonts.googleapis.com/css2?family=Bebas+Neue&family=Archivo:wdth,wght@125,900&family=Open+Sans:wght@400&family=Oswald:wght@700&display=swap">
<style>
  :root {
    --backdrop-center: #5a5a5c;
    --backdrop-edge: #2e2e30;
    --red-dark: #6c0f13;
    --red-mid: #8e161b;
    --red-light: #a81f25;
    --red-band: #be1e2d;
    --swoosh-white: #ffffff;
    --panel-grey: #e6e7e8;
    --ink: #0a0a0a;
    --paper: #ffffff;
  }
  * { margin: 0; padding: 0; box-sizing: border-box; }
  html, body {
    width: 1200px;
    height: 999px;
    overflow: hidden;
  }
  body {
    position: relative;
    background: radial-gradient(ellipse at center, var(--backdrop-center) 0%, var(--backdrop-edge) 100%);
  }
  .sign {
    position: absolute;
    left: 50px;
    top: 133px;
    width: 1096px;
    height: 733px;
    overflow: hidden;
  }
  .sign-shapes {
    position: absolute;
    inset: 0;
    width: 100%;
    height: 100%;
  }
  .sign-text {
    position: absolute;
    left: 0;
    width: 100%;
    text-align: center;
    line-height: 1;
    white-space: nowrap;
  }
  .company-name {
    top: 34px;
    font-family: "Bebas Neue", "Oswald", sans-serif;
    font-size: 196px;
    letter-spacing: 2px;
    color: var(--paper);
  }
  .company-type {
    top: 331px;
    left: -5px;
    font-family: "Archivo", sans-serif;
    font-weight: 900;
    font-stretch: 125%;
    font-size: 90px;
    letter-spacing: 1px;
    color: var(--ink);
  }
  .tagline {
    top: 450px;
    font-family: "Open Sans", sans-serif;
    font-weight: 400;
    font-size: 66px;
    color: var(--ink);
  }
  .phone {
    top: 526px;
    font-family: "Oswald", sans-serif;
    font-weight: 700;
    font-size: 168px;
    letter-spacing: 1px;
    color: var(--ink);
  }
</style>
</head>
<body>
  <section class="sign" aria-label="Marlow Creek Builders job site sign">
    <svg class="sign-shapes" viewBox="0 0 1096 733" preserveAspectRatio="none" aria-hidden="true">
      <defs>
        <linearGradient id="header-red" x1="0" y1="0" x2="0" y2="1">
          <stop offset="0" stop-color="var(--red-dark)"/>
          <stop offset="0.5" stop-color="var(--red-mid)"/>
          <stop offset="1" stop-color="var(--red-light)"/>
        </linearGradient>
      </defs>
      <rect class="header-field" x="0" y="0" width="1096" height="440" fill="url(#header-red)"/>
      <path class="swoosh" d="M0,397 C250,250 700,180 1096,272 L1096,733 L0,733 Z" fill="var(--swoosh-white)"/>
      <path class="info-panel" d="M0,420 C300,280 700,220 1096,337 L1096,733 L0,733 Z" fill="var(--panel-grey)"/>
      <rect class="footer-band" x="0" y="703" width="1096" height="30" fill="var(--red-band)"/>
    </svg>
    <h1 class="sign-text company-name">MARLOW CREEK</h1>
    <p class="sign-text company-type">BUILDERS</p>
    <p class="sign-text tagline">Custom Luxury for Over 20 years</p>
    <p class="sign-text phone">248-555-0137</p>
  </section>
</body>
</html>
```